Postcard Design

We are a home remodeling company we do a complete home remodeling Including bathrooms ,kitchen ,basement ,interior exterior work .
We doing hardwood floors ,painting ,ceramic tile, baseboards ,casings ,Doors ,drywall repairs, plumbing ,electric,etc ,pretty much everything that has to do with interior and exterior remodeling including Room Additions and New Construction.

As far as the colors and design we would like to keep our company colors.
The attachment I sent with the form that I filled in the Tumbix man it's Representing us us as a company as what we do .
Those are the colors that we would like to keep on the flyer so people could recognize us.

Target Market(s)

We would like to target people ho are doing remodeling like kitchen and bathrooms ,basement then people who needs repair and service calls throughout their homes.

Industry/Entity Type

Construction

```html
<!DOCTYPE html>
<html lang="en">
<head>
<meta charset="utf-8">
<title>Hearthwell Remodeling Postcard</title>
<link rel="stylesheet" href="https://fonts.googleapis.com/css2?family=Archivo+Black&family=Arimo:wght@700&family=Gochi+Hand&display=swap">
<style>
  :root {
    --wood-light: #8a7a66;
    --wood-mid: #6b5c4b;
    --wood-dark: #4a3f34;
    --note: #f2ecd9;
    --ink-red: #b3222a;
    --headline-red: #e0262b;
    --white: #ffffff;
    --brand-green: #1f4d2a;
    --pin: #d42a2a;
    --figure-blue: #2f56b8;
    --figure-yellow: #f2c21b;
  }
  html, body {
    margin: 0;
    padding: 0;
    width: 1200px;
    height: 729px;
    overflow: hidden;
    background: #ffffff;
  }
  .postcard {
    position: relative;
    width: 1200px;
    height: 729px;
    overflow: hidden;
  }
  .wood-backdrop {
    position: absolute;
    inset: 0;
    background: radial-gradient(ellipse at 45% 45%, var(--wood-light) 0%, var(--wood-mid) 55%, var(--wood-dark) 100%);
  }
  .note {
    position: absolute;
    background: var(--note);
    box-shadow: 3px 5px 10px rgba(0,0,0,0.35);
    font-family: "Gochi Hand", cursive;
    color: var(--ink-red);
    display: flex;
    align-items: center;
    justify-content: center;
    text-align: center;
    line-height: 1.0;
    font-size: 34px;
    box-sizing: border-box;
    padding: 14px;
  }
  .pin {
    position: absolute;
    width: 16px;
    height: 16px;
    border-radius: 50%;
    background: var(--pin);
    box-shadow: 2px 3px 3px rgba(0,0,0,0.35);
    top: -4px;
  }
  .note-gutters  { left: -60px; top: 52px;  width: 180px; height: 160px; transform: rotate(-14deg); justify-content: flex-end; }
  .note-deck     { left: 160px; top: 28px;  width: 235px; height: 150px; transform: rotate(-12deg); }
  .note-patch    { left: 488px; top: -18px; width: 225px; height: 125px; transform: rotate(-8deg); }
  .note-kitchen  { left: 1060px; top: 262px; width: 200px; height: 165px; transform: rotate(-20deg); justify-content: flex-start; }
  .note-faucet   { left: -70px; top: 355px; width: 185px; height: 155px; transform: rotate(-12deg); justify-content: flex-end; }
  .note-fence    { left: -40px; top: 572px; width: 240px; height: 165px; transform: rotate(-12deg); justify-content: flex-end; }
  .note-guest    { left: 218px; top: 540px; width: 232px; height: 160px; transform: rotate(-12deg); }
  .note-drip     { left: 484px; top: 600px; width: 248px; height: 160px; transform: rotate(-18deg); align-items: flex-start; }

  .headline {
    position: absolute;
    margin: 0;
    left: 95px;
    top: 150px;
    width: 540px;
    transform: rotate(-26deg);
    transform-origin: 50% 50%;
    font-family: "Archivo Black", sans-serif;
    font-weight: 400;
    line-height: 0.9;
    text-shadow: 2px 3px 4px rgba(0,0,0,0.35);
    white-space: nowrap;
  }
  .headline span { display: block; }
  .headline .so-many   { color: var(--white); font-size: 66px; padding-left: 120px; }
  .headline .projects  { color: var(--white); font-size: 78px; padding-left: 40px; }
  .headline .so-little { color: var(--headline-red); font-size: 72px; padding-left: 30px; }
  .headline .time      { color: var(--headline-red); font-size: 130px; padding-left: 110px; line-height: 0.85; }

  .mascot {
    position: absolute;
    left: 700px;
    top: 60px;
    width: 360px;
    height: 400px;
    border-radius: 40px;
    background: linear-gradient(160deg, var(--figure-yellow) 0%, var(--figure-blue) 55%, var(--figure-yellow) 100%);
  }

  .brand-note {
    position: absolute;
    left: 745px;
    top: 545px;
    width: 455px;
    height: 145px;
    background: var(--note);
    box-shadow: 3px 5px 10px rgba(0,0,0,0.35);
    display: flex;
    flex-direction: column;
    align-items: center;
    justify-content: center;
    gap: 14px;
    box-sizing: border-box;
    padding: 0 12px;
  }
  .brand-name {
    display: flex;
    align-items: center;
    gap: 10px;
    font-family: "Arimo", sans-serif;
    font-weight: 700;
    font-size: 27px;
    color: var(--brand-green);
    white-space: nowrap;
  }
  .brand-mark {
    width: 14px;
    height: 14px;
    border-radius: 50%;
    background: var(--brand-green);
  }
  .brand-phone {
    font-family: "Arimo", sans-serif;
    font-weight: 700;
    font-size: 30px;
    color: var(--ink-red);
    white-space: nowrap;
  }
</style>
</head>
<body>
  <main class="postcard">
    <div class="wood-backdrop" role="img" aria-label="Weathered grey-brown wooden board background"></div>

    <div class="note note-gutters"><i class="pin" style="left:30px"></i>inspect and clear gutters</div>
    <div class="note note-deck"><i class="pin" style="left:58px"></i>re-stain<br>the deck</div>
    <div class="note note-patch"><i class="pin" style="left:60px;top:20px"></i>patch<br>wall near<br>back door</div>
    <div class="note note-faucet">fix new<br>faucet<br>drip</div>
    <div class="note note-fence"><i class="pin" style="left:20px"></i>mend<br>hole in<br>fence</div>
    <div class="note note-guest"><i class="pin" style="left:70px"></i>paint<br>walls in<br>guest<br>room</div>
    <div class="note note-drip"><i class="pin" style="left:110px"></i>fix<br>kitchen<br>faucet<br>drip</div>

    <h1 class="headline">
      <span class="so-many">SO MANY</span>
      <span class="projects">PROJECTS</span>
      <span class="so-little">SO LITTLE</span>
      <span class="time">TIME</span>
    </h1>

    <div class="note note-kitchen"><i class="pin" style="left:40px"></i>paint<br>walls<br>in kitchen</div>

    <div class="mascot" role="img" aria-label="Tumbix toy builder in yellow hard hat and blue overalls with tool belt, holding keys in one hand and a small house in the other"></div>

    <div class="brand-note">
      <div class="brand-name"><span class="brand-mark"></span>HEARTHWELL REMODELING</div>
      <div class="brand-phone">+1 555-014-2290</div>
    </div>
  </main>
</body>
</html>
```